Flyer-Design für Dienstleistungen im vorbeugenden Brandschutz und der Ersten Hilfe
Zielgruppe
Wachturm Brandschutz & Erste-Hilfe
Meine Firma spezialisiert sich auf Dienstleistungen im vorbeugenden Brandschutz und im Bereich der Ersten Hilfe.
Mit meiner Firma biete ich folgende Dienstleistungen und Produkte an:
Diensteistungen:
- jährliche Brandschutzunterweisung
- Brandschutzhelferausbildungen nach DGUV Information 205-023
- Brandsicherheitswachen für Unternehmen und Veranstaltungen
- Sanitätsdienste für Unternehmen und Veranstaltungen
- externer Brandschutzbeauftragter
- Vertrieb und Wartung von Feuerlöschern / Brandschutzbedarf
- betriebliche Erste-Hilfe Schulungen / Erste Hilfe Kurs für den Führerschein
- Wartung und Vertrieb von Erste-Hilfe-Material / Ausstattung
- Wartung, Vertrieb und Schulungen von Automatisierten Externen Defibrillatoren
Zu den folgenden Dienstleistungen sollte die Möglichkeit bestehen, detaillierte Texte einzusetzen. Die Themengebite können auch zusammengefasst werden:
Themengebiet 1 (Brandschutz)
Themengebiet 2 (Erste-Hilfe)
Meine Zielgruppe sind primär Firmen, allerdings biete ich die Dienstleistungen auch an Privatpersonen an.
Aufgabenstellung
Die Schriftart in meinem Logo ist 'Avenir'.
Die Firmenfarben orange und grau sollten berücksichtigt werden.
Das Format sollte DIN A4 doppelseitig bedruckt und in 3 Teile gefaltet sein (Ergebnis DIN Lang)
Auf der letzten Seite sollten die Kontaktdaten stehen, sowie mindestens das Logo (Mitglied im BKSV (Bund Kommunaler Sicherheits-Vereine))

```html
<!DOCTYPE html>
<html lang="de">
<head>
<meta charset="utf-8">
<title>Wachturm Sanitätsdienst – Flyer</title>
<link rel="stylesheet" href="https://fonts.googleapis.com/css2?family=Barlow+Semi+Condensed:wght@300;400&display=swap">
<style>
  :root {
    --paper: #e6e6e6;
    --fold: #ffffff;
    --orange: #e8641e;
    --grey: #555555;
    --badge-blue: #2a6ab3;
  }
  html, body {
    margin: 0;
    padding: 0;
    overflow: hidden;
    background: var(--fold);
  }
  .sheet {
    position: relative;
    width: 1200px;
    height: 858px;
    overflow: hidden;
    background: var(--fold);
    font-family: "Barlow Semi Condensed", "Arial Narrow", sans-serif;
    font-weight: 300;
    color: var(--grey);
  }
  .panel {
    position: absolute;
    top: 0;
    height: 858px;
    background: var(--paper);
    overflow: hidden;
  }
  .panel--front { left: 0; width: 592px; }
  .panel--back { left: 607px; width: 593px; }

  .photo {
    position: absolute;
    left: 0;
    top: 0;
    z-index: 0;
  }
  .brand, .text, .heading, .list, .contact, .membership {
    z-index: 1;
  }

  .brand {
    position: absolute;
    top: 18px;
    margin: 0;
    font-weight: 400;
    font-size: 46px;
    line-height: 40px;
    color: var(--orange);
    letter-spacing: 0.5px;
  }
  .brand span { display: block; }

  .text {
    position: absolute;
    margin: 0;
    font-size: 15px;
    line-height: 22.7px;
    letter-spacing: 0.6px;
  }
  .heading {
    position: absolute;
    margin: 0;
    font-weight: 400;
    font-size: 21px;
    line-height: 23px;
    letter-spacing: 1.8px;
    color: var(--orange);
  }
  .list {
    position: absolute;
    margin: 0;
    padding: 0;
    list-style: none;
    font-size: 15px;
    line-height: 22.7px;
    letter-spacing: 0.6px;
  }
  .list li {
    position: relative;
    padding-left: 9px;
  }
  .list li::before {
    content: "";
    position: absolute;
    left: 0;
    top: 8px;
    width: 3px;
    height: 3px;
    border: 1px solid var(--grey);
    border-radius: 50%;
  }
  .list--spaced li { margin-bottom: 6.5px; }

  .contact {
    position: absolute;
    left: 157px;
    top: 766px;
    margin: 0;
    font-style: normal;
    font-size: 15px;
    line-height: 22.7px;
    letter-spacing: 0.6px;
  }
  .membership {
    position: absolute;
    left: 465px;
    top: 770px;
    width: 96px;
    text-align: center;
  }
  .membership__note {
    margin: 0 0 4px;
    font-size: 6px;
    font-weight: 400;
    letter-spacing: 0.2px;
    color: #333;
  }
  .membership__badge {
    width: 92px;
    height: 44px;
    margin: 0 auto;
    border: 2px solid var(--badge-blue);
    box-sizing: border-box;
  }
</style>
</head>
<body>
<div class="sheet">

  <!-- Front panel -->
  <section class="panel panel--front">
    <svg class="photo" width="592" height="858" viewBox="0 0 592 858">
      <defs>
        <linearGradient id="extinguisherTones" x1="0" y1="0" x2="0.4" y2="1">
          <stop offset="0" stop-color="#b8b2ab"/>
          <stop offset="0.45" stop-color="#c9a8a2"/>
          <stop offset="0.7" stop-color="#d8282c"/>
          <stop offset="1" stop-color="#a8161b"/>
        </linearGradient>
        <linearGradient id="trainingTones" x1="0" y1="0" x2="1" y2="1">
          <stop offset="0" stop-color="#cfd8cf"/>
          <stop offset="0.5" stop-color="#e7e3df"/>
          <stop offset="1" stop-color="#d73a3a"/>
        </linearGradient>
      </defs>
      <polygon role="img" aria-label="Foto: Hand prüft mit einem Stift das Manometer eines roten Feuerlöschers" points="414,82 592,129 592,472 327,404" fill="url(#extinguisherTones)"/>
      <polygon role="img" aria-label="Foto: Erste-Hilfe-Kurs, Ausbilderin zeigt Herzdruckmassage an einer Übungspuppe" points="0,560 275,525 317,797 34,834" fill="url(#trainingTones)"/>
    </svg>

    <h1 class="brand" style="left:36px;"><span>Wachturm</span><span>Sanitätsdienst</span></h1>

    <p class="text" style="left:36px; top:111px;">Dienstleistungen im vorbeugenden Brandschutz<br>und im Bereich der Ersten Hilfe</p>

    <p class="text" style="left:36px; top:181px;">Wir setzten dabei auf die hohe Kompetenz und Er-<br>fahrung unserer Mitarbeiter, die alle aus der Feuer-<br>wehr oder aus dem Rettungsdienst kommen.</p>

    <h2 class="heading" style="left:37px; top:308px;">BRANDSCHUTZ</h2>
    <ul class="list list--spaced" style="left:35px; top:346px;">
      <li>jährliche Brandschutzunterweisung</li>
      <li>Brandschutzhelferausbildungen nach<br>DGUV Information 205-023</li>
      <li>Vertrieb und Wartung von Feuerlöschern/<br>Brandschutzbedarf</li>
    </ul>

    <h2 class="heading" style="left:317px; top:582px;">ERSTE HILFE</h2>
    <ul class="list" style="left:315px; top:620px;">
      <li>betriebliche Erste-Hilfe Schulungen/<br>Erste Hilfe Kurs für den Führerschein</li>
      <li>Wartung und Vertrieb von<br>Erste-Hilfe-Material / Ausstattung</li>
      <li>Wartung, Vertrieb und Schulungen<br>von Automatisierten Externen<br>Defibrillatoren</li>
    </ul>
  </section>

  <!-- Back panel -->
  <section class="panel panel--back">
    <svg class="photo" width="593" height="858" viewBox="0 0 593 858">
      <defs>
        <linearGradient id="paramedicTones" x1="0" y1="0" x2="1" y2="1">
          <stop offset="0" stop-color="#d9d9dc"/>
          <stop offset="0.4" stop-color="#c8242a"/>
          <stop offset="0.7" stop-color="#b9bcc4"/>
          <stop offset="1" stop-color="#d42a2e"/>
        </linearGradient>
        <linearGradient id="fireTones" x1="0" y1="0" x2="1" y2="0.3">
          <stop offset="0" stop-color="#e0561a"/>
          <stop offset="0.45" stop-color="#f08a2a"/>
          <stop offset="0.75" stop-color="#c9c6c2"/>
          <stop offset="1" stop-color="#3a3230"/>
        </linearGradient>
      </defs>
      <polygon role="img" aria-label="Foto: Sanitäter in roter Einsatzkleidung versorgen ein Mädchen unter einer Rettungsdecke" points="338,68 593,108 568,342 301,280" fill="url(#paramedicTones)"/>
      <polygon role="img" aria-label="Foto: Flammen werden mit Löschschaum gelöscht" points="0,301 203,244 246,393 34,455" fill="url(#fireTones)"/>
    </svg>

    <h1 class="brand" style="left:37px;"><span>Wachturm</span><span>Sanitätsdienst</span></h1>

    <h2 class="heading" style="left:37px; top:135px;">VERANSTALTUNGSSERVICE<br>SANITÄTER</h2>
    <ul class="list" style="left:37px; top:195px;">
      <li>Sanitätsdienste für Unternehmen<br>und Veranstaltungen</li>
    </ul>

    <h2 class="heading" style="left:265px; top:347px;">VERANSTALTUNGSSERVICE<br>BRANDSICHERHEITSWACHE</h2>
    <ul class="list" style="left:265px; top:403px;">
      <li>Brandsicherheitswachen<br>für Unternehmen und Veranstaltungen</li>
    </ul>

    <h2 class="heading" style="left:37px; top:479px;">DIENSTLEISTUNGEN</h2>
    <ul class="list" style="left:37px; top:511px;">
      <li>jährliche Brandschutzunterweisung</li>
      <li>Brandschutzhelferausbildungen nach DGUV Information 205-023</li>
      <li>Brandsicherheitswachen für Unternehmen und Veranstaltungen</li>
      <li>Sanitätsdienste für Unternehmen und Veranstaltungen</li>
      <li>externer Brandschutzbeauftragter</li>
      <li>Vertrieb und Wartung von Feuerlöschern / Brandschutzbedarf</li>
      <li>betriebliche Erste-Hilfe Schulungen / Erste Hilfe Kurs für den Führerschein</li>
      <li>Wartung und Vertrieb von Erste-Hilfe-Material / Ausstattung</li>
      <li>Wartung, Vertrieb und Schulungen von Automatisierten Externen Defibrillatoren</li>
    </ul>

    <address class="contact">
      Wachturm Brandschutz<br>
      Lindenhofweg 4 / 24103 Musterstadt<br>
      info@wachturm-bs.de / 0176 - 00 12 34 56
    </address>

    <div class="membership">
      <p class="membership__note">Dieses Unternehmen ist Mitglied im</p>
      <div class="membership__badge" role="img" aria-label="Mitgliedszeichen Bund Kommunaler Sicherheits-Vereine"></div>
    </div>
  </section>

</div>
</body>
</html>
```